Rinsely Surface Cleaning - Business Card Design

Use company logo and design a new business card. We are looking for a front and back design. The back should be a dark purple background. We want the back to show cartoon-like soap bubbles chasing mildew cartoon shaped figures. This gives the idea that Rinsely Surface Cleaning provides exterior washing services that work. No mildew stands a chance when Rinsely Surface Cleaning shows up to work. The mildew cartoon images should be green in color, have eyes, and look scared of the bubbles. The bubbles should be light blue in color and have eyes that looked excited to be there.
We will advertise on Chatterly and Pixalonia. These Chatterly and Pixalonia icons should be somewhere on the card.

```html
<!DOCTYPE html>
<html lang="en">
<head>
<meta charset="utf-8">
<title>Rinsely Surface Cleaning – Business Card</title>
<link href="https://fonts.googleapis.com/css2?family=Nunito:wght@400;700;900&display=swap" rel="stylesheet">
<style>
  :root {
    --purple: #35206a;
    --purple-deep: #2b1a58;
    --accent-blue: #4a5bd0;
    --name-blue: #6c72d8;
    --bubble-blue: #bfe6f7;
    --mildew-green: #7dd13c;
    --white: #ffffff;
    --page: #f2f2f4;
    --text-dark: #2b1a58;
  }
  * { margin: 0; padding: 0; box-sizing: border-box; }
  html, body {
    width: 1200px; height: 523px; overflow: hidden;
    background: var(--page);
    font-family: "Nunito", sans-serif;
  }
  .canvas {
    position: relative; width: 1200px; height: 523px;
    display: flex; align-items: center; justify-content: center; gap: 40px;
  }
  .card {
    position: relative; width: 540px; height: 320px; overflow: hidden;
    box-shadow: 0 2px 10px rgba(0,0,0,.15);
  }
  /* Front */
  .card--front { background: var(--white); }
  .front-shape { position: absolute; inset: 0; }
  .contact {
    position: absolute; left: 34px; top: 100px; color: var(--white);
  }
  .contact__name {
    font-weight: 900; font-size: 22px; letter-spacing: .3px;
    color: var(--name-blue); text-transform: uppercase;
  }
  .contact__title { font-size: 12px; margin-top: 2px; margin-bottom: 14px; }
  .contact__line {
    display: flex; align-items: center; gap: 8px;
    font-size: 11px; line-height: 18px;
  }
  .contact__line svg { width: 10px; height: 10px; flex: none; }
  .front-brand {
    position: absolute; right: 22px; top: 118px; width: 220px; text-align: center;
    color: var(--text-dark); font-weight: 900; font-size: 30px; line-height: 1.05;
  }
  /* Back */
  .card--back { background: var(--purple); }
  .back-art {
    position: absolute; inset: 0;
    background:
      radial-gradient(circle at 18% 22%, rgba(191,230,247,.35) 0 22px, transparent 24px),
      radial-gradient(circle at 72% 20%, rgba(191,230,247,.35) 0 22px, transparent 24px),
      radial-gradient(circle at 88% 62%, rgba(191,230,247,.3) 0 20px, transparent 22px),
      radial-gradient(circle at 24% 82%, rgba(191,230,247,.3) 0 20px, transparent 22px),
      radial-gradient(circle at 34% 18%, rgba(125,209,60,.4) 0 20px, transparent 22px),
      radial-gradient(circle at 88% 32%, rgba(125,209,60,.4) 0 22px, transparent 24px),
      radial-gradient(circle at 12% 62%, rgba(125,209,60,.4) 0 18px, transparent 20px),
      radial-gradient(circle at 72% 84%, rgba(125,209,60,.45) 0 30px, transparent 32px),
      var(--purple);
  }
  .back-brand {
    position: absolute; left: 0; right: 0; top: 108px; text-align: center;
    color: var(--white); font-weight: 900; font-size: 40px; line-height: 1.05;
  }
  .socials {
    position: absolute; left: 0; right: 0; top: 222px;
    display: flex; justify-content: center; gap: 18px;
    color: var(--white); font-size: 13px; font-weight: 700;
  }
  .social { display: flex; align-items: center; gap: 6px; }
  .social__dot {
    width: 16px; height: 16px; border-radius: 50%; background: var(--white);
  }
</style>
</head>
<body>
<main class="canvas">
  <section class="card card--front" aria-label="Business card front side">
    <svg class="front-shape" viewBox="0 0 540 320" preserveAspectRatio="none">
      <path d="M0 0 H420 C330 40 250 150 320 320 H0 Z" fill="var(--purple)"/>
      <path d="M420 0 C330 40 250 150 320 320" fill="none" stroke="var(--accent-blue)" stroke-width="5" transform="translate(10 0)"/>
    </svg>
    <div class="contact">
      <div class="contact__name">Marcus Delgado</div>
      <div class="contact__title">President</div>
      <div class="contact__line">
        <svg viewBox="0 0 10 10"><path d="M2 1 L4 1 L4.6 3 L3.5 3.8 C4 5 5 6 6.2 6.5 L7 5.4 L9 6 L9 8 C5 8.5 1.5 5 2 1 Z" fill="var(--white)"/></svg>
        555-014-2277
      </div>
      <div class="contact__line">
        <svg viewBox="0 0 10 10"><rect x="1" y="2" width="8" height="6" fill="var(--accent-blue)"/></svg>
        marcus@rinselyclean.com
      </div>
      <div class="contact__line">
        <svg viewBox="0 0 10 10"><circle cx="5" cy="5" r="3.6" fill="none" stroke="var(--accent-blue)" stroke-width="1.2"/></svg>
        rinselyclean.com
      </div>
    </div>
    <div class="front-brand">Rinsely Surface Cleaning</div>
  </section>

  <section class="card card--back" aria-label="Business card back side">
    <div class="back-art" role="img" aria-label="Cartoon light blue soap bubbles chasing scared green mildew figures on dark purple"></div>
    <div class="back-brand">Rinsely<br>Surface Cleaning</div>
    <div class="socials">
      <span class="social"><span class="social__dot"></span>Chatterly</span>
      <span class="social"><span class="social__dot"></span>Pixalonia</span>
    </div>
  </section>
</main>
</body>
</html>
```